Opal Meadow Signage

Please I'm looking to have signage for business front door and 2 windows. Wow me! It is the first thing ppl will see always.
I'm looking to have some privacy because I am in the beauty business, so privacy is key. Please look at attached pictures of front and windows. Make it elegant because the spa shop is all about luxury excellence. I need website, Email address phone number in name of the company. I'd like to also put some services somewhere on the signage (s) you can place it where you'd think it would be best. Lymphatic Drainage, Body Sculpting/contouring, Detoxing, Cavitation, Facials ..... and much more

```html
<!DOCTYPE html>
<html lang="en">
<head>
<meta charset="utf-8">
<title>Opal Meadow Signage</title>
<link rel="stylesheet" href="https://fonts.googleapis.com/css2?family=Lexend:wght@400;500&family=Montserrat:wght@500;600&display=swap">
<style>
  :root {
    --navy: #1b1aa6;
    --violet: #6a1bff;
    --paper: #ffffff;
    --backdrop: #e9e9ec;
    --flora-a: #e6dcff;
    --flora-b: #f7f3ff;
  }
  * { margin: 0; padding: 0; box-sizing: border-box; }
  html, body { width: 1200px; height: 1001px; overflow: hidden; }
  body {
    position: relative;
    background: var(--backdrop);
    font-family: "Lexend", sans-serif;
    color: var(--navy);
  }
  .sign {
    position: absolute;
    background: var(--paper);
    overflow: hidden;
    box-shadow: 0 2px 10px rgba(0,0,0,0.12);
  }
  .flora {
    position: absolute;
    border-radius: 40%;
    background: radial-gradient(ellipse at center, var(--flora-a) 0%, var(--flora-b) 70%, transparent 100%);
  }
  .centered {
    position: absolute;
    left: 0; right: 0;
    text-align: center;
  }
  .mark-dot {
    position: absolute;
    border-radius: 50%;
    background: var(--navy);
  }
  .brand {
    color: var(--violet);
    font-weight: 400;
    text-transform: uppercase;
    line-height: 1;
    letter-spacing: -0.5px;
  }
  .tagline {
    font-family: "Montserrat", sans-serif;
    font-weight: 600;
    text-transform: uppercase;
    color: var(--navy);
  }
  .divider {
    position: absolute;
    left: 50%;
    height: 2px;
    background: var(--violet);
    transform: translateX(-50%);
  }
  .divider::after {
    content: "";
    position: absolute;
    left: 50%; top: 50%;
    width: 6px; height: 6px;
    background: var(--navy);
    transform: translate(-50%, -50%) rotate(45deg);
  }

  /* Suite plate */
  .suite-plate {
    left: 122px; top: 164px; width: 219px; height: 61px;
    display: flex; align-items: center; justify-content: center;
    font-size: 31px; font-weight: 400; letter-spacing: 1px;
  }

  /* Door panel */
  .door-panel { left: 144px; top: 296px; width: 176px; height: 524px; }
  .door-panel .brand { top: 226px; font-size: 31px; }
  .door-panel .tagline { top: 303px; font-size: 12px; line-height: 15px; letter-spacing: 0.3px; }
  .door-panel .contact { font-size: 10.5px; line-height: 16px; }
  .door-panel .contact .phone { font-size: 11.5px; }

  /* Services window */
  .services-panel { left: 374px; top: 162px; width: 263px; height: 592px; }
  .service {
    position: absolute; left: 0; right: 0;
    text-align: center;
    font-size: 19px;
    line-height: 20px;
    font-weight: 400;
  }

  /* Banner window */
  .banner-panel { left: 656px; top: 152px; width: 438px; height: 195px; }
  .banner-panel .brand { top: 113px; font-size: 24px; }
  .banner-panel .tagline { top: 139px; font-size: 7.5px; letter-spacing: 0.2px; }
  .banner-panel .web { top: 163px; font-size: 15px; color: var(--violet); letter-spacing: 0.3px; }
</style>
</head>
<body>

  <div class="sign suite-plate">SUITE F</div>

  <section class="sign door-panel">
    <div class="flora" style="left:74px;top:-6px;width:108px;height:82px" role="img" aria-label="Line-art leafy branch with buds in violet, top corner"></div>
    <div class="mark-dot" style="left:48px;top:126px;width:80px;height:80px"></div>
    <div class="centered brand">Opal<br>Meadow</div>
    <div class="centered tagline">Where beauty<br>wellness find<br>harmony</div>
    <div class="divider" style="top:360px;width:98px"></div>
    <div class="centered contact" style="top:373px">
      <div class="phone">(212) 555-0148</div>
      <div>hello@opalmeadow.com</div>
      <div>www.opalmeadow.com</div>
    </div>
    <div class="flora" style="left:-6px;top:444px;width:130px;height:86px" role="img" aria-label="Line-art flower and leafy branch in violet, bottom corner"></div>
  </section>

  <section class="sign services-panel">
    <div class="flora" style="left:-6px;top:-6px;width:116px;height:92px" role="img" aria-label="Line-art leafy branch with berries in violet, top corner"></div>
    <div class="service" style="top:173px">Lymphatic Drainage</div>
    <div class="divider" style="top:203px;width:78px"></div>
    <div class="service" style="top:217px">Body Sculpting<br>Contouring</div>
    <div class="divider" style="top:265px;width:78px"></div>
    <div class="service" style="top:280px">Detoxing</div>
    <div class="divider" style="top:308px;width:78px"></div>
    <div class="service" style="top:316px">Cavitation</div>
    <div class="divider" style="top:344px;width:78px"></div>
    <div class="service" style="top:352px">Facials</div>
    <div class="divider" style="top:380px;width:78px"></div>
    <div class="service" style="top:388px">...and Much More</div>
    <div class="flora" style="left:40px;top:436px;width:230px;height:162px" role="img" aria-label="Line-art leaves, berries and flowing stems in violet, lower half"></div>
  </section>

  <section class="sign banner-panel">
    <div class="flora" style="left:-6px;top:-6px;width:80px;height:60px" role="img" aria-label="Line-art flower and leaves in violet, top corner"></div>
    <div class="mark-dot" style="left:190px;top:30px;width:58px;height:58px"></div>
    <div class="centered brand">Opal Meadow</div>
    <div class="centered tagline">Where beauty wellness find harmony</div>
    <div class="centered web">www.opalmeadow.com</div>
    <div class="flora" style="left:334px;top:116px;width:110px;height:85px" role="img" aria-label="Line-art leafy branch with bud in violet, bottom corner"></div>
  </section>

</body>
</html>
```